POP/ROCK artist: CD Cover Design Project

IF U LOVE MUSIC AND ALBUM COVER ART THEN PLEASE PARTICIPATE IN MY PROJECT AND HAVE A GREAT TIME DESIGNING SOMETHING UNIQUE AND EXCITING!!!!
Hi, my name is tovo, a pop/rock artist living in Europe. i just finished recording a fun dance song, called FIZZY PAPER KITES, with a successful Quenmarsh Studios producer in Europe and I just put the finishing touches on the music video shot in LA. Now i'm going to release the song and video with Brivasong. It's going to go out to about 750 stores, including Plinkr, strumbly and all the other biggies as well as a load of smaller ones.
I need a great looking CD cover design that i can plaster everywhere . . . and i really mean everywhere i can.
As per Brivasong' specs, the cover art MUST BE 1500 x 1500 pixels. It cannot be blurry or pixilated and must be perfectly square.
I've uploaded some pics for you to choose from but you can use whichever one(s) you like . . . or none of them if you prefer, according to your inspiration. Just let me know if you want other pics and i can upload others.
Updates
Hey there,
Hey there,
Hi again, all,
Hey there,
Reason: Some designers are still revising their designs and we need more time.
Hi there, designers!
Hello everybody,
Target Market(s)
Modern pop/rock radio listeners of Tamblewick Radio, QFX, etc.
Please click on the following link to see the music video and hear the song:
http://www.vidcastro.example/watch?v=Qp7rTm2LwZa
Also, i have various pics and photos i can upload . . . just tell me what you need!!!!!
Requirements
Must have
- As per Brivasong' specs, the cover art MUST BE 1500 x 1500 pixels. It cannot be blurry or pixilated and must be perfectly square.
My artist name, tovo, and the song title, Fizzy Paper Kites, must be on the cover art.
The destination for your design is online music stores like Plinkr. So the dimensions will be VERY SMALL The actual size seen by the public will be about 1.5 cm x 1.5 cm! (Please have a look at the Plinkr store to see the actual size people will view the designs in.)
This means that your designs have to be clearly communicated at that size. The title of the song (fizzy paper kites) and my artist name (tovo) have to be large enough to read and whatever idea you're going for has to be easily understood.
Nice to have
- It should look totally modern and pop/rock, hip and cool. It's up to you and your design magic to do whatever you think it takes.
Should not have
- Website and e-mail addresses CANNOT be included anywhere on cover art.

```html
<!DOCTYPE html>
<html lang="en">
<head>
<meta charset="utf-8">
<title>tovo — Fizzy Paper Kites</title>
<link rel="stylesheet" href="https://fonts.googleapis.com/css2?family=Saira+Stencil+One&family=Stardos+Stencil:wght@700&display=swap">
<style>
  :root {
    --ink: #000000;
    --paper: #ffffff;
    --title-grey: #7a7a7a;
    --photo-top: #6a6a6a;
    --photo-mid: #0d0d0d;
    --photo-low: #d2d2d2;
  }
  html, body {
    margin: 0;
    padding: 0;
    width: 1200px;
    height: 1200px;
    overflow: hidden;
    background: var(--ink);
  }
  .cover {
    position: relative;
    width: 1200px;
    height: 1200px;
    background: var(--ink);
    overflow: hidden;
  }
  .photo-strips {
    position: absolute;
    inset: 0;
  }
  .artist-name {
    position: absolute;
    left: 60px;
    top: 505px;
    margin: 0;
    font-family: "Stardos Stencil", "Stencil", serif;
    font-weight: 700;
    font-size: 230px;
    line-height: 1;
    letter-spacing: -6px;
    color: var(--paper);
  }
  .song-title {
    position: absolute;
    left: 64px;
    top: 728px;
    margin: 0;
    font-family: "Saira Stencil One", "Stencil", sans-serif;
    font-weight: 400;
    font-size: 118px;
    line-height: 98px;
    letter-spacing: 0;
    color: var(--title-grey);
    text-transform: uppercase;
  }
  .song-title span { display: block; }
</style>
</head>
<body>
<main class="cover">
  <svg class="photo-strips" width="1200" height="1200" viewBox="0 0 1200 1200" role="img" aria-label="Repeated vertical slices of a black-and-white photo of the artist in sunglasses playing guitar">
    <defs>
      <linearGradient id="strip-tone" x1="0" y1="0" x2="0" y2="1">
        <stop offset="0" stop-color="var(--photo-top)" />
        <stop offset="0.26" stop-color="#3a3a3a" />
        <stop offset="0.38" stop-color="var(--photo-mid)" />
        <stop offset="0.88" stop-color="var(--photo-mid)" />
        <stop offset="0.94" stop-color="#8a8a8a" />
        <stop offset="1" stop-color="var(--photo-low)" />
      </linearGradient>
    </defs>
    <g class="strip-set" fill="url(#strip-tone)">
      <rect x="0" y="0" width="70" height="1200" />
      <rect x="74" y="0" width="160" height="1200" />
      <rect x="238" y="0" width="224" height="1200" />
      <rect x="466" y="0" width="228" height="1200" />
      <rect x="700" y="0" width="96" height="1200" />
      <rect x="800" y="0" width="66" height="1200" />
      <rect x="872" y="0" width="328" height="1200" />
    </g>
    <g class="accent-lines" fill="var(--paper)">
      <rect x="694" y="0" width="4" height="770" />
      <rect x="851" y="470" width="19" height="730" />
      <rect x="1140" y="435" width="4" height="765" />
    </g>
  </svg>

  <h1 class="artist-name">tovo</h1>
  <h2 class="song-title">
    <span>Fizzy</span>
    <span>Paper</span>
    <span>Kites</span>
  </h2>
</main>
</body>
</html>
```